Silver Lumen Med Spa Membership Sales Presentation to Clients handout

Hello! We are a high tech, Silver Lumen Med Spa in Dallas Texas that won Best Med Spa in Addison. I want my graphic membership form to represent that. We serve women and men so want it neutral but show cutting edge. Our colors are black, white, gray but would entertain your view. Having a challenge on making it easy to read as each membership gets more services yet one service a month. Thought maybe colorcoding what services are together? Definite road blocks on my end. I used Canva to lay out, but as you can see I am NOT gifted at graphic design. ;))

Target Market(s)

39-69

Industry/Entity Type

Medical Med Spa

Requirements
Must have
• cutting edge look

```html
<!DOCTYPE html>
<html lang="en">
<head>
<meta charset="UTF-8">
<title>Silver Lumen Med Spa – Ever Radiant Memberships</title>
<link href="https://fonts.googleapis.com/css2?family=Montserrat:wght@400;500;700;800&display=swap" rel="stylesheet">
<style>
:root{
  --ink:#0b0b0e;
  --white:#ffffff;
  --row:#e3e3e3;
  --text:#161616;
  --check:#333333;
  --green:#218a3a;
  --blue:#2386ad;
  --purple:#7b2180;
  --dark:#222222;
  --navy:#2c4596;
  --copper:#a85e2a;
}
*{margin:0;padding:0;box-sizing:border-box}
html,body{width:849px;height:1200px;overflow:hidden;background:var(--white)}
body{font-family:'Montserrat',sans-serif;color:var(--text)}
.sheet{position:relative;width:849px;height:1200px;overflow:hidden}

.masthead{position:absolute;left:0;top:0;width:849px;height:203px;background:var(--ink)}
.brand{position:absolute;left:40px;top:60px;width:150px;color:var(--white);font-weight:500;font-size:19px;line-height:1.25;letter-spacing:.5px}
.brand-mark{display:block;width:22px;height:22px;border:2px solid var(--white);border-radius:50%;margin-bottom:10px}
.divider{position:absolute;left:201px;top:37px;width:2px;height:137px;background:var(--white)}
.title{position:absolute;left:228px;top:72px;color:var(--white);font-weight:700;font-size:31.5px;line-height:32px;letter-spacing:.6px}
.award{position:absolute;left:660px;top:30px;width:160px;height:190px}

.table-head{position:absolute;left:51px;top:247px;width:744px;height:50px}
.table-head h2{font-weight:800;font-size:22px;letter-spacing:.4px}
.table-head p{font-size:14.8px;letter-spacing:.3px;margin-top:2px}
.tier{position:absolute;top:0;text-align:center;width:110px}
.tier b{display:block;font-weight:800;font-size:22px;line-height:23px}
.tier span{display:block;font-size:22px;line-height:23px}
.tier.good{left:439px}.tier.better{left:547px}.tier.best{left:646px}

.treatments{position:absolute;left:51px;top:307px;width:744px}
.row{display:flex;height:22px;margin-bottom:5.55px}
.swatch{width:25px;height:22px}
.name{width:420px;background:var(--row);font-size:13px;line-height:23px;padding-left:17px;letter-spacing:.5px;font-weight:500}
.cell{background:var(--row);margin-left:2px;display:flex;align-items:center;justify-content:center;font-size:13px;letter-spacing:.2px}
.cell small{font-size:8.5px;margin-left:3px;letter-spacing:.4px}
.c1{width:99px}.c2{width:99px}.c3{width:95px}
.tick{width:16px;height:14px;margin-top:-5px}
.g{background:var(--green)}.b{background:var(--blue)}.p{background:var(--purple)}
.d{background:var(--dark)}.n{background:var(--navy)}.o{background:var(--copper)}

.contact{position:absolute;left:41px;top:1156px;font-weight:700;font-size:14.5px;letter-spacing:.2px}
.contact .sep{font-weight:400;margin:0 8px}
.footer-band{position:absolute;left:0;top:0}
.web{position:absolute;left:500px;width:349px;top:1148px;text-align:center;color:var(--white);font-weight:700;font-size:21.5px;letter-spacing:.4px}
</style>
</head>
<body>
<div class="sheet">
  <svg width="0" height="0" style="position:absolute">
    <symbol id="tick" viewBox="0 0 16 14"><path d="M1 7.5 L5.5 12 L15 1.5" fill="none" stroke="var(--check)" stroke-width="2.6" stroke-linejoin="miter"/></symbol>
  </svg>

  <header class="masthead">
    <div class="brand"><span class="brand-mark"></span>Silver Lumen Med Spa</div>
    <div class="divider"></div>
    <h1 class="title">EVER RADIANT<br>MEMBERSHIPS</h1>
  </header>
  <svg class="award" viewBox="0 0 160 190" role="img" aria-label="Award badge">
    <circle cx="79" cy="110" r="78" fill="var(--ink)"/>
    <rect x="2" y="4" width="156" height="152" fill="var(--ink)"/>
    <circle cx="78" cy="80" r="70" fill="none" stroke="var(--white)" stroke-width="1.5"/>
  </svg>

  <div class="table-head">
    <h2>TREATMENTS</h2>
    <p>(GREEN IS UNLIMITED + ONE COLOR PER MONTH)</p>
    <div class="tier good"><b>GOOD</b><span>$189</span></div>
    <div class="tier better"><b>BETTER</b><span>$289</span></div>
    <div class="tier best"><b>BEST</b><span>$389</span></div>
  </div>

  <section class="treatments">
    <div class="row"><div class="swatch g"></div><div class="name">SKIN EVALUATION</div><div class="cell c1"><svg class="tick"><use href="#tick"/></svg></div><div class="cell c2"><svg class="tick"><use href="#tick"/></svg></div><div class="cell c3"><svg class="tick"><use href="#tick"/></svg></div></div>
    <div class="row"><div class="swatch g"></div><div class="name">INFRARED SAUNA</div><div class="cell c1"><svg class="tick"><use href="#tick"/></svg></div><div class="cell c2"><svg class="tick"><use href="#tick"/></svg></div><div class="cell c3"><svg class="tick"><use href="#tick"/></svg></div></div>
    <div class="row"><div class="swatch g"></div><div class="name">MASSAGE CHAIR</div><div class="cell c1"><svg class="tick"><use href="#tick"/></svg></div><div class="cell c2"><svg class="tick"><use href="#tick"/></svg></div><div class="cell c3"><svg class="tick"><use href="#tick"/></svg></div></div>
    <div class="row"><div class="swatch g"></div><div class="name">VIBRATIONAL LYMPHATIC PLATE</div><div class="cell c1"><svg class="tick"><use href="#tick"/></svg></div><div class="cell c2"><svg class="tick"><use href="#tick"/></svg></div><div class="cell c3"><svg class="tick"><use href="#tick"/></svg></div></div>
    <div class="row"><div class="swatch b"></div><div class="name">MEDICAL FACIAL</div><div class="cell c1"><svg class="tick"><use href="#tick"/></svg></div><div class="cell c2"><svg class="tick"><use href="#tick"/></svg></div><div class="cell c3"><svg class="tick"><use href="#tick"/></svg></div></div>
    <div class="row"><div class="swatch b"></div><div class="name">FACE LYMPHATIC DRAINAGE</div><div class="cell c1"><svg class="tick"><use href="#tick"/></svg></div><div class="cell c2"><svg class="tick"><use href="#tick"/></svg></div><div class="cell c3"><svg class="tick"><use href="#tick"/></svg></div></div>
    <div class="row"><div class="swatch b"></div><div class="name">RED LIGHT THERAPY</div><div class="cell c1"><svg class="tick"><use href="#tick"/></svg></div><div class="cell c2"><svg class="tick"><use href="#tick"/></svg></div><div class="cell c3"><svg class="tick"><use href="#tick"/></svg></div></div>
    <div class="row"><div class="swatch b"></div><div class="name">PH OXYGEN SERU</div><div class="cell c1"><svg class="tick"><use href="#tick"/></svg></div><div class="cell c2"><svg class="tick"><use href="#tick"/></svg></div><div class="cell c3"><svg class="tick"><use href="#tick"/></svg></div></div>
    <div class="row"><div class="swatch p"></div><div class="name">CHEMICAL PEELS PROGRESSIVE OR MIDDEPTH</div><div class="cell c1"><svg class="tick"><use href="#tick"/></svg></div><div class="cell c2"><svg class="tick"><use href="#tick"/></svg></div><div class="cell c3"><svg class="tick"><use href="#tick"/></svg></div></div>
    <div class="row"><div class="swatch d"></div><div class="name">ORVEX BROADBAND RENEW</div><div class="cell c1"><svg class="tick"><use href="#tick"/></svg></div><div class="cell c2"><svg class="tick"><use href="#tick"/></svg></div><div class="cell c3"><svg class="tick"><use href="#tick"/></svg></div></div>
    <div class="row"><div class="swatch d"></div><div class="name">ORVEX 2 CORRECTION PASSES</div><div class="cell c1"><svg class="tick"><use href="#tick"/></svg></div><div class="cell c2"><svg class="tick"><use href="#tick"/></svg></div><div class="cell c3"><svg class="tick"><use href="#tick"/></svg></div></div>
    <div class="row"><div class="swatch b"></div><div class="name">DERMAPLANING</div><div class="cell c1"></div><div class="cell c2"><svg class="tick"><use href="#tick"/></svg></div><div class="cell c3"><svg class="tick"><use href="#tick"/></svg></div></div>
    <div class="row"><div class="swatch b"></div><div class="name">VITAMIN A PEEL</div><div class="cell c1"></div><div class="cell c2"><svg class="tick"><use href="#tick"/></svg></div><div class="cell c3"><svg class="tick"><use href="#tick"/></svg></div></div>
    <div class="row"><div class="swatch d"></div><div class="name">ORVEX UO TO 10 CORRECTION PASSES</div><div class="cell c1"></div><div class="cell c2"><svg class="tick"><use href="#tick"/></svg></div><div class="cell c3"><svg class="tick"><use href="#tick"/></svg></div></div>
    <div class="row"><div class="swatch d"></div><div class="name">ORVEX HAIR REMOVAL</div><div class="cell c1"></div><div class="cell c2"><svg class="tick"><use href="#tick"/></svg></div><div class="cell c3"><svg class="tick"><use href="#tick"/></svg></div></div>
    <div class="row"><div class="swatch n"></div><div class="name">MICRONEEDLING</div><div class="cell c1"></div><div class="cell c2"><svg class="tick"><use href="#tick"/></svg></div><div class="cell c3"><svg class="tick"><use href="#tick"/></svg></div></div>
    <div class="row"><div class="swatch o"></div><div class="name">ORVEX FIRM PULSE</div><div class="cell c1"></div><div class="cell c2"></div><div class="cell c3"><svg class="tick"><use href="#tick"/></svg></div></div>
    <div class="row"><div class="swatch n"></div><div class="name">MICRONEEDLING GLOWTHREAD</div><div class="cell c1"></div><div class="cell c2"></div><div class="cell c3"><svg class="tick"><use href="#tick"/></svg></div></div>
    <div class="row"><div class="swatch p"></div><div class="name">CHEMICAL PEEL VELLURA ITALIAN</div><div class="cell c1"></div><div class="cell c2"></div><div class="cell c3"><svg class="tick"><use href="#tick"/></svg></div></div>
    <div class="row"><div class="swatch g"></div><div class="name">VELTARA TARGETED WEIGHT LOSS</div><div class="cell c1"></div><div class="cell c2"></div><div class="cell c3"><svg class="tick"><use href="#tick"/></svg></div></div>
    <div class="row"><div class="swatch d"></div><div class="name">LASER REJUVENATION</div><div class="cell c1">10%<small>OFF</small></div><div class="cell c2">20%<small>OFF</small></div><div class="cell c3">30%<small>OFF</small></div></div>
    <div class="row"><div class="swatch d"></div><div class="name">PLASMA PEN</div><div class="cell c1">10%<small>OFF</small></div><div class="cell c2">20%<small>OFF</small></div><div class="cell c3">30%<small>OFF</small></div></div>
    <div class="row"><div class="swatch d"></div><div class="name">HYPERBARIC OXYGEN</div><div class="cell c1">10%<small>OFF</small></div><div class="cell c2">20%<small>OFF</small></div><div class="cell c3">30%<small>OFF</small></div></div>
    <div class="row"><div class="swatch d"></div><div class="name">MASSAGE</div><div class="cell c1">10%<small>OFF</small></div><div class="cell c2">20%<small>OFF</small></div><div class="cell c3">30%<small>OFF</small></div></div>
    <div class="row"><div class="swatch d"></div><div class="name">AIRBRUSH TANNING</div><div class="cell c1">10%<small>OFF</small></div><div class="cell c2">20%<small>OFF</small></div><div class="cell c3">30%<small>OFF</small></div></div>
    <div class="row"><div class="swatch d"></div><div class="name">IONIC DETOX</div><div class="cell c1">10%<small>OFF</small></div><div class="cell c2">20%<small>OFF</small></div><div class="cell c3">30%<small>OFF</small></div></div>
    <div class="row"><div class="swatch d"></div><div class="name">LYMPHATIC DRAINAGE</div><div class="cell c1">10%<small>OFF</small></div><div class="cell c2">20%<small>OFF</small></div><div class="cell c3">30%<small>OFF</small></div></div>
    <div class="row"><div class="swatch d"></div><div class="name">TIRZEPATIDE WEIGHT LOSS PEPTIDE</div><div class="cell c1">10%<small>OFF</small></div><div class="cell c2">20%<small>OFF</small></div><div class="cell c3">30%<small>OFF</small></div></div>
    <div class="row"><div class="swatch d"></div><div class="name">LIP FILLERS NEEDLE-LESS</div><div class="cell c1">10%<small>OFF</small></div><div class="cell c2">20%<small>OFF</small></div><div class="cell c3">30%<small>OFF</small></div></div>
  </section>

  <footer>
    <p class="contact">214.555.0142<span class="sep">|</span>880 Larkspur Ave. Plano, TX 75024</p>
    <svg class="footer-band" width="849" height="1200" viewBox="0 0 849 1200" aria-hidden="true"><polygon points="501,1140 849,1140 849,1200 434,1200" fill="var(--ink)"/></svg>
    <p class="web">SILVERLUMENMEDSPA.COM</p>
  </footer>
</div>
</body>
</html>
```